Criação de Kit com 6 Layouts de Post para Redes Sociais (Facebook, Instagram e etc) + Capa de Facebook para Outros
" Atualmente, on-line. Estamos abertos há poucos meses, fazendo atendimento para outras agencias e agora vamos abrir para atendimento do público utilizando instagram, whatsapp e face como formas de captação. "

```html
<!DOCTYPE html>
<html lang="pt-BR">
<head>
<meta charset="UTF-8">
<title>Descubra os melhores destinos</title>
<link rel="stylesheet" href="https://fonts.googleapis.com/css2?family=Poppins:wght@400;500;600;700&display=swap">
<style>
  :root {
    --sky-top: #eef3f8;
    --sky-bottom: #dfe8f1;
    --brand-blue: #1d8fe6;
    --navy: #16305a;
    --ink: #2b2f36;
    --white: #ffffff;
    --dash: #2a8de0;
  }
  * { margin: 0; padding: 0; box-sizing: border-box; }
  html, body { width: 1200px; height: 1200px; overflow: hidden; }
  body { font-family: "Poppins", sans-serif; }
  .post {
    position: relative;
    width: 1200px;
    height: 1200px;
    overflow: hidden;
    background: radial-gradient(ellipse at 70% 30%, #ffffff 0%, var(--sky-top) 45%, var(--sky-bottom) 100%);
  }
  .route-lines { position: absolute; inset: 0; }
  .destination-photo {
    position: absolute;
    left: 89px;
    width: 470px;
    border-radius: 26px;
  }
  .destination-photo.beach { top: -20px; height: 404px; background: linear-gradient(180deg, #8fc3e8 0%, #5fb0d2 45%, #7f9a64 80%, #a98660 100%); }
  .destination-photo.mountain { top: 401px; height: 391px; background: linear-gradient(180deg, #f3b38a 0%, #d3a6a4 40%, #8a7c74 75%, #5a8fb0 100%); }
  .destination-photo.coast { top: 809px; height: 411px; background: linear-gradient(180deg, #a9cde6 0%, #5aa9a2 40%, #2a96ac 70%, #8fae72 100%); }
  .brand-name {
    position: absolute;
    left: 703px;
    top: 236px;
    font-size: 31px;
    font-weight: 600;
    color: var(--brand-blue);
    letter-spacing: 0.5px;
  }
  .headline {
    position: absolute;
    left: 703px;
    top: 296px;
    font-size: 62px;
    line-height: 74px;
    font-weight: 600;
    color: var(--brand-blue);
  }
  .subhead {
    position: absolute;
    left: 703px;
    top: 700px;
    font-size: 37px;
    line-height: 50px;
    font-weight: 400;
    color: var(--ink);
  }
  .cta {
    position: absolute;
    left: 703px;
    top: 924px;
    height: 60px;
    display: flex;
    align-items: stretch;
  }
  .cta-icon {
    width: 64px;
    background: var(--navy);
    display: flex;
    align-items: center;
    justify-content: center;
  }
  .cta-label {
    background: var(--brand-blue);
    color: var(--white);
    font-size: 22px;
    font-weight: 500;
    display: flex;
    align-items: center;
    padding: 0 18px 0 16px;
  }
</style>
</head>
<body>
  <main class="post">
    <svg class="route-lines" width="1200" height="1200" viewBox="0 0 1200 1200" aria-hidden="true">
      <g fill="none" stroke="var(--dash)" stroke-width="3" stroke-dasharray="14 10" stroke-linecap="round">
        <path d="M0 50 Q50 80 100 110"/>
        <path d="M560 110 Q760 40 960 80 Q1120 115 1200 260"/>
        <path d="M860 1200 Q960 1030 1200 930"/>
      </g>
    </svg>

    <div class="destination-photo beach" role="img" aria-label="Praia com mar azul e morros verdes; viajante de chapéu e vestido preto em primeiro plano"></div>
    <div class="destination-photo mountain" role="img" aria-label="Montanha rochosa à beira-mar ao entardecer; viajante sentada sobre mala dourada olhando o celular"></div>
    <div class="destination-photo coast" role="img" aria-label="Vista aérea de enseada com águas turquesa"></div>

    <div class="brand-name">SEU LOGO</div>
    <h1 class="headline">Descubra os<br>melhores<br>destinos<br>com a gente!</h1>
    <p class="subhead">Conheça lugares<br>incríveis para<br>passar suas férias!</p>

    <div class="cta">
      <span class="cta-icon">
        <svg width="22" height="28" viewBox="0 0 22 28" aria-hidden="true">
          <path d="M5 3 L16 14 L5 25" fill="none" stroke="#ffffff" stroke-width="4" stroke-linecap="round" stroke-linejoin="round"/>
        </svg>
      </span>
      <span class="cta-label">Fale conosco agora!</span>
    </div>
  </main>
</body>
</html>
```